I want a business card that is going to show a creative spark but without limiting me to an industry. Something edgy but that wont go out of date. I want it state My business name Serafina Loire, profession - Professional Makeup Artist contact number and email

My service is to provide makeup services from bridal, fashion, photography, film, TV and so on. It is creative and different so i want that to be reflected.

I would like the card double sided.
Updates

 I would LOVE a background on my card something like this image... i can supply an image to be formed like this

Please use the image uploaded

Can we try using the image provided on one side of the card and then writing and details on the other side

Target Market(s)

I am targeting a wide range of people from Creative directors to the individual eg. bride

Industry/Entity Type

Business

Requirements
Must have
• Name: Delphine Hartwell
contact numbe 0417853120
email address:info@serafinaloire.com
website: www.serafinaloire.com
One of the images attached

professional makeup artist / hair stylist

I want it to show creativity
Nice to have
• logo, Double-sided card
Should not have
• the design should not use tradional style. Or images that are not my own

```html
<!DOCTYPE html>
<html lang="en">
<head>
<meta charset="utf-8">
<title>Serafina Loire – Business Card</title>
<link href="https://fonts.googleapis.com/css2?family=Lato:wght@300;400;700&display=swap" rel="stylesheet">
<style>
  :root {
    --backdrop: #9b9b9b;
    --card-grey: #e6e6e6;
    --card-cream: #fdf7e0;
    --card-black: #0a0a0a;
    --ink: #111111;
    --paper-text: #e8e8e8;
  }
  * { box-sizing: border-box; margin: 0; padding: 0; }
  html, body {
    width: 1200px;
    height: 733px;
    overflow: hidden;
    background: var(--backdrop);
    font-family: "Lato", sans-serif;
  }
  .sheet { position: relative; width: 1200px; height: 733px; }
  .card {
    position: absolute;
    width: 505px;
    height: 303px;
  }
  .card--front-grey  { left: 48px;  top: 48px;  background: var(--card-grey); }
  .card--front-cream { left: 649px; top: 48px;  background: var(--card-cream); }
  .card--back-left   { left: 48px;  top: 386px; background: var(--card-black); }
  .card--back-right  { left: 649px; top: 386px; background: var(--card-black); }

  /* Front */
  .front-mark {
    position: absolute;
    left: 50%;
    top: 96px;
    width: 34px;
    height: 34px;
    margin-left: 6px;
    border-radius: 50%;
    background: var(--ink);
  }
  .front-name {
    position: absolute;
    left: 0; right: 0;
    top: 168px;
    text-align: center;
    color: var(--ink);
    font-size: 38px;
    font-weight: 400;
    letter-spacing: 0.5px;
    padding-left: 12px;
  }
  .front-role {
    position: absolute;
    left: 0; right: 0;
    top: 233px;
    text-align: center;
    color: var(--ink);
    font-size: 10px;
    font-weight: 700;
    letter-spacing: 0.2px;
    padding-left: 10px;
  }

  /* Back */
  .back-details {
    position: absolute;
    right: 30px;
    top: 180px;
    text-align: right;
    color: var(--paper-text);
  }
  .back-role {
    font-size: 11.5px;
    font-weight: 300;
    letter-spacing: 0.3px;
  }
  .back-name {
    font-size: 27px;
    font-weight: 400;
    color: #ffffff;
    line-height: 1.15;
    margin-top: 2px;
  }
  .back-line {
    display: flex;
    justify-content: flex-end;
    align-items: center;
    gap: 6px;
    font-size: 11.5px;
    font-weight: 300;
    margin-top: 3px;
  }
  .back-line svg { flex: none; }
</style>
</head>
<body>
<main class="sheet">

  <section class="card card--front-grey" aria-label="Card front, grey">
    <span class="front-mark" aria-hidden="true"></span>
    <p class="front-name">Serafina Loire</p>
    <p class="front-role">PROFESSIONAL MAKEUP ARTIST</p>
  </section>

  <section class="card card--front-cream" aria-label="Card front, cream">
    <span class="front-mark" aria-hidden="true"></span>
    <p class="front-name">Serafina Loire</p>
    <p class="front-role">PROFESSIONAL MAKEUP ARTIST</p>
  </section>

  <section class="card card--back-left" aria-label="Card back">
    <div class="back-details">
      <p class="back-role">PROFESSIONAL MAKEUP ARTIST</p>
      <p class="back-name">Serafina Loire</p>
      <p class="back-line">
        <svg width="10" height="13" viewBox="0 0 10 13" aria-hidden="true">
          <rect x="0.6" y="0.6" width="8.8" height="11.8" rx="1" fill="none" stroke="#e8e8e8" stroke-width="1.2"/>
          <rect x="2.2" y="2.2" width="5.6" height="2.6" fill="#e8e8e8"/>
          <g fill="#e8e8e8"><rect x="2.2" y="6.2" width="1.5" height="1.5"/><rect x="4.3" y="6.2" width="1.5" height="1.5"/><rect x="6.3" y="6.2" width="1.5" height="1.5"/><rect x="2.2" y="8.8" width="1.5" height="1.5"/><rect x="4.3" y="8.8" width="1.5" height="1.5"/><rect x="6.3" y="8.8" width="1.5" height="1.5"/></g>
        </svg>
        0417853120
      </p>
      <p class="back-line">
        <svg width="16" height="11" viewBox="0 0 16 11" aria-hidden="true">
          <rect x="0.6" y="0.6" width="14.8" height="9.8" fill="none" stroke="#e8e8e8" stroke-width="1.2"/>
          <path d="M0.8 0.8 L8 6 L15.2 0.8" fill="none" stroke="#e8e8e8" stroke-width="1.2"/>
        </svg>
        info@serafinaloire.com
      </p>
    </div>
  </section>

  <section class="card card--back-right" aria-label="Card back">
    <div class="back-details">
      <p class="back-role">PROFESSIONAL MAKEUP ARTIST</p>
      <p class="back-name">Serafina Loire</p>
      <p class="back-line">
        <svg width="10" height="13" viewBox="0 0 10 13" aria-hidden="true">
          <rect x="0.6" y="0.6" width="8.8" height="11.8" rx="1" fill="none" stroke="#e8e8e8" stroke-width="1.2"/>
          <rect x="2.2" y="2.2" width="5.6" height="2.6" fill="#e8e8e8"/>
          <g fill="#e8e8e8"><rect x="2.2" y="6.2" width="1.5" height="1.5"/><rect x="4.3" y="6.2" width="1.5" height="1.5"/><rect x="6.3" y="6.2" width="1.5" height="1.5"/><rect x="2.2" y="8.8" width="1.5" height="1.5"/><rect x="4.3" y="8.8" width="1.5" height="1.5"/><rect x="6.3" y="8.8" width="1.5" height="1.5"/></g>
        </svg>
        0417853120
      </p>
      <p class="back-line">
        <svg width="16" height="11" viewBox="0 0 16 11" aria-hidden="true">
          <rect x="0.6" y="0.6" width="14.8" height="9.8" fill="none" stroke="#e8e8e8" stroke-width="1.2"/>
          <path d="M0.8 0.8 L8 6 L15.2 0.8" fill="none" stroke="#e8e8e8" stroke-width="1.2"/>
        </svg>
        info@serafinaloire.com
      </p>
    </div>
  </section>

</main>
</body>
</html>
```